Vornel Estates - Chat n’ Cheer Thursday Graphic Invite

We need a graphic design for a corporate reception that we are calling Chat n’ Cheer Thursday. The invite should read:

"QBR invites you to join us at Chat n’ Cheer Thursday

Monday, Jan 22nd
6:30 - 8:30 pm EST

Copper Ladle - Lounge Room

48210 E Pelican Grove Rd
Aventura, FL 33180

Join us for excellent wine and tasty bites at our semi-annual DAW reception. Swing by whenever you can – timing is casual and we'd love to see you there!"

Please feel free to use fun photos from the Copper Ladle gallery: https://www.copperladlegrill.com/photos

Also, please use the QBR logo attached.

Target Market(s)

Corporate professional

Colors
0054AA
0677BA
7BADD7
CADEEF
E8F1F8

Requirements
Must have
• QBR logo, attached verbiage

```html
<!DOCTYPE html>
<html lang="en">
<head>
<meta charset="utf-8">
<title>QBR – Chat n’ Cheer Thursday Invite</title>
<link href="https://fonts.googleapis.com/css2?family=Nunito+Sans:ital,wght@0,300;0,400;0,700;0,800;1,700;1,800&family=Playball&display=swap" rel="stylesheet">
<style>
  :root {
    --table-dark: #3b2a1e;
    --table-mid: #8a6444;
    --table-light: #b58c66;
    --panel: rgba(236, 232, 230, 0.82);
    --ink-gold: #7a5615;
    --brand-navy: #0d3a8c;
    --brand-blue: #0677ba;
    --badge-dark: #231f20;
    --badge-text: #f4f1ec;
  }
  html, body {
    margin: 0;
    padding: 0;
    width: 857px;
    height: 1200px;
    overflow: hidden;
    background: #ffffff;
  }
  .invite {
    position: relative;
    width: 857px;
    height: 1200px;
    overflow: hidden;
    font-family: "Nunito Sans", Arial, sans-serif;
    color: var(--ink-gold);
  }
  .invite__backdrop {
    position: absolute;
    inset: 0;
    background:
      radial-gradient(ellipse at 15% 20%, rgba(255,255,255,0.35), transparent 40%),
      radial-gradient(ellipse at 90% 60%, rgba(255,255,255,0.4), transparent 35%),
      linear-gradient(160deg, var(--table-light) 0%, var(--table-mid) 45%, var(--table-dark) 100%);
  }
  .invite__panel {
    position: absolute;
    left: 97px;
    top: 0;
    width: 659px;
    height: 1200px;
    background: var(--panel);
  }
  .line {
    position: absolute;
    left: 97px;
    width: 659px;
    margin: 0;
    text-align: center;
    white-space: nowrap;
  }
  .brand {
    position: absolute;
    left: 0;
    width: 857px;
    top: 76px;
    display: flex;
    justify-content: center;
    align-items: center;
    gap: 14px;
  }
  .brand__mark {
    width: 58px;
    height: 58px;
    background: var(--brand-blue);
  }
  .brand__name {
    font-weight: 800;
    font-size: 64px;
    line-height: 70px;
    color: var(--brand-navy);
    letter-spacing: 1px;
  }
  .lead {
    top: 216px;
    font-weight: 700;
    font-size: 33px;
    line-height: 38px;
  }
  .title {
    font-family: "Playball", "Brush Script MT", cursive;
    font-weight: 400;
    font-size: 88px;
    line-height: 100px;
  }
  .title--first { top: 256px; }
  .title--second { top: 360px; font-size: 94px; }
  .note {
    font-weight: 400;
    font-size: 22px;
    line-height: 30px;
  }
  .note--wine { top: 484px; }
  .note--reception { top: 514px; }
  .note--casual { top: 550px; }
  .note--guests { top: 580px; }
  .detail {
    font-weight: 800;
    font-size: 24px;
    line-height: 34px;
  }
  .detail--date { top: 634px; }
  .detail--time { top: 668px; }
  .detail--venue { top: 726px; }
  .detail--room { top: 760px; }
  .detail--street { top: 818px; }
  .detail--city { top: 852px; }
  .venue-host {
    top: 894px;
    font-weight: 800;
    font-style: italic;
    font-size: 17px;
    line-height: 24px;
  }
  .rsvp {
    top: 980px;
    font-weight: 800;
    font-style: italic;
    font-size: 22px;
    line-height: 30px;
  }
  .venue-badge {
    position: absolute;
    left: 289px;
    top: 1026px;
    width: 275px;
    height: 150px;
    background: var(--badge-dark);
    display: flex;
    align-items: center;
    justify-content: center;
  }
  .venue-badge__name {
    font-family: "Nunito Sans", Arial, sans-serif;
    font-weight: 700;
    font-size: 15px;
    letter-spacing: 6px;
    color: var(--badge-text);
    text-transform: uppercase;
  }
</style>
</head>
<body>
  <main class="invite">
    <div class="invite__backdrop" role="img" aria-label="Overhead photo of a wooden restaurant table set with steak on a board, seafood, salads and glasses of wine"></div>
    <div class="invite__panel"></div>

    <div class="brand">
      <span class="brand__mark"></span>
      <span class="brand__name">QBR</span>
    </div>

    <p class="line lead">Join us for</p>
    <h1 class="line title title--first">Chat n’ Cheer</h1>
    <p class="line title title--second">Thursday</p>

    <p class="line note note--wine">Join us for excellent wine and tasty bites</p>
    <p class="line note note--reception">at our semi-annual DAW reception.</p>
    <p class="line note note--casual">Timing is casual and we'd love to see you there.</p>
    <p class="line note note--guests">Guests welcome!</p>

    <p class="line detail detail--date">Monday, Jan. 22nd</p>
    <p class="line detail detail--time">6:30 - 8:30 PM EST</p>

    <p class="line detail detail--venue">Copper Ladle</p>
    <p class="line detail detail--room">Lounge Room</p>

    <p class="line detail detail--street">48210 E Pelican Grove Rd</p>
    <p class="line detail detail--city">Aventura, FL 33180</p>
    <p class="line venue-host">located in the Harborline Grand Aventura</p>

    <p class="line rsvp">Kindly RSVP by 1/17</p>

    <div class="venue-badge">
      <span class="venue-badge__name">Copper Ladle</span>
    </div>
  </main>
</body>
</html>
```